Business Card Design Project for New Home Builder

Double sided card,
Larger logo on 1 side with small quote, Its not just a house, Its your Home, across the bottom. Matt Red base, White logo, black quote??

other side, ,
Its your Home LHS. Smaller logo RHS with.
Details below.

"neuropolitical Rg" Logo Font

Derek Hollins

PO Box 7384 Mildura VIC 3502
Mobile 0427 318950 / Phone 03 50871 639 / Fax 03 50871 982
email DerekH@wvbuilds.net.au
Vic Building Practitioner DB-U 8147 Vic Commercial Builder CB-U 5093
NSW Contractor Reg 67318C

Target Market(s)

New Home Buyers

Industry/Entity Type

Business

Requirements
Must have
• Sharp detail, Red Black & White colourings.
Should not have
• Any new colours

```html
<!DOCTYPE html>
<html lang="en">
<head>
<meta charset="utf-8">
<title>Westvale Builds – Business Card</title>
<link href="https://fonts.googleapis.com/css2?family=Michroma&family=Questrial&display=swap" rel="stylesheet">
<style>
  :root {
    --red: #d9181d;
    --red-light: #e5363a;
    --red-dark: #c3141a;
    --white: #ffffff;
    --ice: #e6f0f5;
    --ink: #1b1b1b;
    --page: #efefef;
  }
  * { box-sizing: border-box; margin: 0; padding: 0; }
  html, body { width: 1200px; height: 760px; overflow: hidden; }
  body { background: var(--page); position: relative; font-family: "Questrial", sans-serif; }

  .card {
    position: absolute;
    width: 600px;
    height: 343px;
    overflow: hidden;
    box-shadow: 0 10px 28px rgba(0,0,0,0.22);
  }

  /* Front side */
  .card--front {
    left: 70px; top: 40px;
    background: linear-gradient(110deg, var(--red-dark) 0%, var(--red) 55%, var(--red-light) 100%);
  }
  .brand-front {
    position: absolute; left: 0; right: 0; top: 118px;
    text-align: center; color: var(--white);
    font-family: "Michroma", sans-serif; font-size: 34px; letter-spacing: 1px;
  }
  .tagline-band {
    position: absolute; left: 0; right: 0; bottom: 0; height: 58px;
    background: var(--ice);
    display: flex; align-items: flex-start; justify-content: center;
  }
  .tagline-strip {
    width: 100%; height: 24px; background: var(--white);
    display: flex; align-items: center; justify-content: center;
    color: var(--red); font-size: 15px; letter-spacing: 0.5px;
    border-bottom: 1px solid #cfdde4;
  }

  /* Back side */
  .card--back {
    left: 530px; top: 405px;
    background: var(--white);
  }
  .back-red { position: absolute; inset: 0; }
  .motto {
    position: absolute; left: 30px; top: 32px;
    color: var(--red); font-size: 11px; letter-spacing: 1px;
  }
  .person-name {
    position: absolute; left: 30px; top: 70px;
    color: var(--red); font-family: "Michroma", sans-serif; font-size: 22px;
  }
  .brand-back {
    position: absolute; right: 26px; top: 28px;
    color: var(--red); font-family: "Michroma", sans-serif; font-size: 12px;
  }
  .contacts {
    position: absolute; left: 30px; top: 178px; list-style: none;
    color: var(--white); font-size: 12.5px; line-height: 1.3;
  }
  .contacts li { display: flex; align-items: flex-start; gap: 10px; margin-bottom: 8px; }
  .contacts svg { width: 11px; height: 11px; flex: none; margin-top: 2px; }
  .registrations {
    position: absolute; left: 300px; top: 226px; width: 280px;
    color: var(--white); font-size: 11px; line-height: 1.35;
  }
</style>
</head>
<body>

<section class="card card--front" aria-label="Card front">
  <div class="brand-front">WESTVALE BUILDS</div>
  <div class="tagline-band">
    <p class="tagline-strip">It's not just a house, It's your Home</p>
  </div>
</section>

<section class="card card--back" aria-label="Card back">
  <svg class="back-red" viewBox="0 0 600 343" preserveAspectRatio="none" aria-hidden="true">
    <defs>
      <linearGradient id="backRed" x1="0" y1="0" x2="1" y2="0">
        <stop offset="0" stop-color="#c3141a"/>
        <stop offset="0.6" stop-color="#d9181d"/>
        <stop offset="1" stop-color="#e5363a"/>
      </linearGradient>
    </defs>
    <polygon points="0,165 600,105 600,343 0,343" fill="url(#backRed)"/>
  </svg>

  <p class="motto">IT'S YOUR HOME</p>
  <h1 class="person-name">DEREK HOLLINS</h1>
  <p class="brand-back">WESTVALE BUILDS</p>

  <ul class="contacts">
    <li>
      <svg viewBox="0 0 12 12"><path d="M6 0.5a4 4 0 0 1 4 4c0 3-4 7-4 7s-4-4-4-7a4 4 0 0 1 4-4z" fill="#fff"/><circle cx="6" cy="4.5" r="1.4" fill="#d9181d"/></svg>
      <span>PO Box 7384 Mildura VIC 3502</span>
    </li>
    <li>
      <svg viewBox="0 0 12 12"><path d="M3 1l2 2.5-1.2 1.3c.6 1.4 1.8 2.6 3.2 3.2L8.3 6.8 11 9l-1.3 2C5 11 1 7 1 2.3z" fill="#fff"/></svg>
      <span>+0427 318950/03 50871 639<br>
      03 50871 982</span>
    </li>
    <li>
      <svg viewBox="0 0 12 12"><rect x="1" y="3" width="10" height="8" rx="1" fill="none" stroke="#fff"/><path d="M1.5 3.5 6 7l4.5-3.5" fill="none" stroke="#fff"/></svg>
      <span>DerekH@wvbuilds.net.au</span>
    </li>
  </ul>

  <p class="registrations">Vic Building Practitioner DB-U 8147 Vic Commercial Builder CB-U 5093<br>
  NSW Contractor Reg 67318C</p>
</section>

</body>
</html>
```